Rack card for a integrative medical practice

Need an eye-catching rack card with our logo with content as provided. We have a membership based holistic medical practice which incorporates western and holistic medicine. We would like to focus on wellness and healthy lifestyle. See uploaded files for what is included in the membership. Would like 2 page rack card color on both sides. Logo must be on the front.

Target Market(s)

People looking for alternative medicine, healthy lifestyle.

Industry/Entity Type

Health and Wellness

Colors
00AB8E
00BBA5
67D7C9
C6EFE9
E9F9F6

Requirements
Must have
• Must spark interest at first sight. Clear message.
Nice to have
• Warm, bright and positive vibe. Organic, neutral and earthy colors.
Should not have
• Traditional medical practice vibe (cold, formal, industrial). No PINK except the logo.

```html
<!DOCTYPE html>
<html lang="en">
<head>
<meta charset="utf-8">
<title>Sage Grove Health &amp; Wellness — Rack Card</title>
<link rel="stylesheet" href="https://fonts.googleapis.com/css2?family=Marcellus&family=Marcellus+SC&family=Raleway:wght@400;500&family=Open+Sans:wght@400;600;700&display=swap">
<style>
  :root {
    --page-bg: #e4e6e2;
    --card-bg: #f3f6f1;
    --sage: #98a997;
    --sage-dark: #7f917e;
    --frame-line: #c8dbb6;
    --ink: #2b2d2b;
    --ink-soft: #3d403d;
    --pill: #4a4c4a;
    --white: #ffffff;
    --brand: #2f4a40;
  }
  * { box-sizing: border-box; margin: 0; padding: 0; }
  html, body { width: 1200px; height: 900px; overflow: hidden; }
  body {
    background: var(--page-bg);
    display: flex;
    align-items: center;
    justify-content: center;
    gap: 60px;
  }
  .rack-card {
    position: relative;
    width: 365px;
    height: 820px;
    background: var(--card-bg);
    overflow: hidden;
    box-shadow: 0 6px 18px rgba(0,0,0,0.18);
  }
  .card-frame {
    position: absolute;
    inset: 12px;
    border: 1.5px solid var(--frame-line);
    pointer-events: none;
    z-index: 3;
  }
  .hero {
    display: block;
    width: 365px;
  }
  .card-body {
    position: relative;
    z-index: 2;
    text-align: center;
    color: var(--ink);
  }
  /* front */
  .brand-mark {
    display: flex;
    align-items: center;
    justify-content: center;
    gap: 10px;
    margin-top: 12px;
  }
  .brand-dot {
    width: 14px; height: 14px;
    border-radius: 50%;
    background: var(--brand);
  }
  .brand-name {
    font-family: "Marcellus", serif;
    font-size: 30px;
    letter-spacing: 3px;
    color: var(--brand);
  }
  .practice-title {
    font-family: "Marcellus", serif;
    font-size: 28px;
    font-weight: 400;
    margin-top: 44px;
  }
  .practice-tagline {
    font-family: "Marcellus SC", serif;
    font-size: 15px;
    line-height: 1.75;
    letter-spacing: 0.5px;
    margin-top: 34px;
    color: var(--ink-soft);
  }
  /* back */
  .back-title {
    font-family: "Marcellus", serif;
    font-size: 25px;
    font-weight: 400;
    margin-top: 6px;
  }
  .membership-heading {
    font-family: "Marcellus", serif;
    font-size: 24px;
    font-weight: 400;
    text-align: left;
    line-height: 1.2;
    padding: 0 26px;
    margin-top: 16px;
    color: var(--ink);
  }
  .benefit-list {
    list-style: none;
    text-align: left;
    padding: 0 24px 0 26px;
    margin-top: 12px;
  }
  .benefit-list li {
    position: relative;
    font-family: "Raleway", sans-serif;
    font-size: 13.5px;
    line-height: 1.3;
    color: var(--ink-soft);
    padding-left: 22px;
    margin-bottom: 11px;
  }
  .benefit-list li::before {
    content: "";
    position: absolute;
    left: 2px; top: 4px;
    width: 10px; height: 10px;
    border-radius: 50%;
    background: var(--sage);
  }
  /* footer */
  .contact-band {
    position: absolute;
    left: 0; right: 0; bottom: 0;
    height: 112px;
    background: var(--sage);
    border-top: 6px solid var(--frame-line);
    z-index: 2;
    text-align: center;
    font-family: "Open Sans", sans-serif;
    color: var(--white);
  }
  .contact-pill {
    position: absolute;
    left: 50%;
    top: -26px;
    transform: translateX(-50%);
    display: flex;
    align-items: center;
    gap: 8px;
    white-space: nowrap;
    background: var(--pill);
    color: var(--white);
    border-radius: 20px;
    padding: 7px 20px;
    font-size: 13px;
    font-weight: 600;
  }
  .contact-pill .label { text-transform: uppercase; }
  .phone-icon { width: 15px; height: 15px; }
  .contact-web {
    margin-top: 24px;
    font-size: 15px;
    font-weight: 700;
  }
  .contact-address {
    margin-top: 4px;
    font-size: 13px;
  }
</style>
</head>
<body>

  <!-- Front side -->
  <article class="rack-card rack-card--front">
    <svg class="hero" viewBox="0 0 365 390" width="365" height="390">
      <defs>
        <linearGradient id="lakeGradient" x1="0" y1="0" x2="0" y2="1">
          <stop offset="0" stop-color="#cfe0ea"/>
          <stop offset="0.35" stop-color="#a9c2cf"/>
          <stop offset="0.55" stop-color="#8aa6b4"/>
          <stop offset="1" stop-color="#5f7d8c"/>
        </linearGradient>
        <radialGradient id="frontSun" cx="0.42" cy="0.45" r="0.35">
          <stop offset="0" stop-color="#fff6dc" stop-opacity="0.9"/>
          <stop offset="1" stop-color="#fff6dc" stop-opacity="0"/>
        </radialGradient>
      </defs>
      <g role="img" aria-label="Photo: woman with open arms standing on a rock at a sunlit mountain lake">
        <path d="M0 0 H365 V250 Q182 440 0 250 Z" fill="url(#lakeGradient)"/>
        <path d="M0 0 H365 V250 Q182 440 0 250 Z" fill="url(#frontSun)"/>
      </g>
      <path d="M0 250 Q182 440 365 250 V285 Q182 460 0 295 Z" fill="var(--sage)"/>
    </svg>

    <div class="card-body">
      <div class="brand-mark">
        <span class="brand-dot"></span>
        <span class="brand-name">Sage Grove</span>
      </div>
      <h1 class="practice-title">Sage Grove Health &amp; Wellness</h1>
      <p class="practice-tagline">
        A direct primary care practice<br>
        focused on a more holistic<br>
        and personal approach to medicine.
      </p>
    </div>

    <footer class="contact-band">
      <div class="contact-pill">
        <span class="label">Contact us</span>
        <svg class="phone-icon" viewBox="0 0 24 24" aria-hidden="true">
          <circle cx="12" cy="12" r="10.5" fill="none" stroke="currentColor" stroke-width="1.8"/>
          <path d="M9 7.5l1.6 2.4-1 1.2c.7 1.4 1.7 2.4 3.1 3.1l1.2-1 2.4 1.6-.8 1.6c-3.6-.3-7-3.7-7.3-7.3z" fill="currentColor"/>
        </svg>
        <span>(555) 014-2870</span>
      </div>
      <p class="contact-web">www.sagegrovehealth.com</p>
      <p class="contact-address">1420 Elm Ridge Rd., STE 2B Fairview</p>
    </footer>
    <div class="card-frame"></div>
  </article>

  <!-- Back side -->
  <article class="rack-card rack-card--back">
    <svg class="hero" viewBox="0 0 365 270" width="365" height="270">
      <defs>
        <linearGradient id="stonesGradient" x1="0" y1="0" x2="0" y2="1">
          <stop offset="0" stop-color="#e9e0d0"/>
          <stop offset="0.5" stop-color="#d8c3a0"/>
          <stop offset="1" stop-color="#8a7a68"/>
        </linearGradient>
        <radialGradient id="backSun" cx="0.6" cy="0.35" r="0.35">
          <stop offset="0" stop-color="#fff4d6" stop-opacity="0.95"/>
          <stop offset="1" stop-color="#fff4d6" stop-opacity="0"/>
        </radialGradient>
      </defs>
      <g role="img" aria-label="Photo: stacked stones labelled mind, body, soul at sunset by the water">
        <path d="M0 0 H365 V150 Q182 330 0 150 Z" fill="url(#stonesGradient)"/>
        <path d="M0 0 H365 V150 Q182 330 0 150 Z" fill="url(#backSun)"/>
      </g>
      <path d="M0 150 Q182 330 365 150 V180 Q182 345 0 195 Z" fill="var(--sage)"/>
    </svg>

    <div class="card-body">
      <h2 class="back-title">Sage Grove Health &amp; Wellness</h2>
      <h3 class="membership-heading">WHAT'S INCLUDED IN YOUR MEMBERSHIP :</h3>
      <ul class="benefit-list">
        <li>Unlimited office visits with no copay</li>
        <li>Direct communication with your doctor</li>
        <li>Discounted labs, imaging and medications</li>
        <li>Free initial acupuncture session ($250 value).</li>
        <li>2 BioScan testings per year ($100 value)</li>
        <li>Discounts for supplements and health products in the clinic</li>
        <li>Discounts for iv vitamin infusion therapy</li>
        <li>Personalized nutrition plan after advanced testing such as gut microbiome, hormonal, metabolism test, etc.</li>
      </ul>
    </div>

    <footer class="contact-band">
      <div class="contact-pill">
        <span class="label">Contact us</span>
        <svg class="phone-icon" viewBox="0 0 24 24" aria-hidden="true">
          <circle cx="12" cy="12" r="10.5" fill="none" stroke="currentColor" stroke-width="1.8"/>
          <path d="M9 7.5l1.6 2.4-1 1.2c.7 1.4 1.7 2.4 3.1 3.1l1.2-1 2.4 1.6-.8 1.6c-3.6-.3-7-3.7-7.3-7.3z" fill="currentColor"/>
        </svg>
        <span>(555) 014-2870</span>
      </div>
      <p class="contact-web">www.sagegrovehealth.com</p>
      <p class="contact-address">1420 Elm Ridge Rd., STE 2B Fairview</p>
    </footer>
    <div class="card-frame"></div>
  </article>

</body>
</html>
```